Informative poster of frozen yogurt prices and sizes

Product is Frozen Yogurt. Need a menu poster A1/A0 size. Graphics showing 3 cup sizes (small $4, Medium $6 & Large $8). Extra 50Cent for each toppings (toppings includes stawberries, kiwi, nuts, candy etc.
for similar concept please refer to www.velmorasweets.com .
Design has to be clear and not too complicated

Target Market(s)

The poster is to be located at high traffic area. therefore it has to be very clear and precise and eye catching

Industry/Entity Type

Product

Requirements
Must have
• graphics of frozen yogurt cup, a variety of topping with prices. The prices has to be bold and clear. Easy to understand and not complicated.
Nice to have
• concept of value for money and healthy option dessert
Should not have
• too complicated background graphic

```html
<!DOCTYPE html>
<html lang="en">
<head>
<meta charset="utf-8">
<title>Frozen Yogurt Price Menu</title>
<link rel="stylesheet" href="https://fonts.googleapis.com/css2?family=Oswald:wght@600;700&display=swap">
<style>
  :root {
    --canvas-bg: #eee6d8;
    --poster-center: #ea1761;
    --poster-mid: #d0136a;
    --poster-edge: #a70e6e;
    --price-green: #a8d814;
    --badge-white: #ffffff;
    --cup-light: #fbf7ef;
    --cup-shade: #e4ddd0;
    --topping-red: #c8283a;
    --text-white: #ffffff;
  }
  * { margin: 0; padding: 0; box-sizing: border-box; }
  html, body { width: 1200px; height: 1000px; overflow: hidden; }
  body {
    background: var(--canvas-bg);
    font-family: "Oswald", "Arial Narrow", sans-serif;
    position: relative;
  }
  .menu-poster {
    position: absolute;
    left: 315px;
    top: 98px;
    width: 570px;
    height: 807px;
    overflow: hidden;
    background: radial-gradient(ellipse 70% 60% at 50% 55%, var(--poster-center) 0%, var(--poster-mid) 55%, var(--poster-edge) 100%);
  }
  .product-photo {
    position: absolute;
    border-radius: 40% 40% 18% 18% / 45% 45% 14% 14%;
    background: linear-gradient(180deg, var(--cup-shade) 0%, var(--cup-light) 40%, var(--cup-light) 70%, var(--cup-shade) 100%);
    box-shadow: inset 0 30px 40px -20px rgba(200, 40, 58, 0.35);
  }
  .product-photo--small  { left: 63px;  top: 90px;  width: 142px; height: 187px; }
  .product-photo--medium { left: 368px; top: 192px; width: 167px; height: 220px; }
  .product-photo--large  { left: 45px;  top: 442px; width: 200px; height: 275px; }

  .price-badge {
    position: absolute;
    border-radius: 50%;
    background: var(--badge-white);
    display: flex;
    flex-direction: column;
    align-items: center;
    justify-content: center;
    color: var(--price-green);
    font-weight: 700;
    text-transform: uppercase;
    line-height: 0.95;
  }
  .price-badge::before {
    content: "";
    position: absolute;
    inset: -10px;
    border: 2px dashed var(--badge-white);
    border-radius: 50%;
  }
  .price-badge--small  { left: 157px; top: 47px;  width: 140px; height: 140px; }
  .price-badge--medium { left: 225px; top: 224px; width: 146px; height: 146px; }
  .price-badge--large  { left: 212px; top: 414px; width: 190px; height: 190px; }

  .price-badge__size { letter-spacing: 0.5px; }
  .price-badge__amount { letter-spacing: 1px; }
  .price-badge--small  .price-badge__size   { font-size: 25px; }
  .price-badge--small  .price-badge__amount { font-size: 64px; }
  .price-badge--medium .price-badge__size   { font-size: 32px; }
  .price-badge--medium .price-badge__amount { font-size: 76px; }
  .price-badge--large  .price-badge__size   { font-size: 40px; }
  .price-badge--large  .price-badge__amount { font-size: 96px; }

  .topping-note {
    position: absolute;
    left: 270px;
    top: 683px;
    width: 290px;
    text-align: center;
    color: var(--text-white);
    font-weight: 700;
    text-transform: uppercase;
    line-height: 1.05;
  }
  .topping-note__price { font-size: 36px; letter-spacing: 0.5px; }
  .topping-note__label { font-size: 22px; }
  .topping-note__list  { font-size: 14.5px; margin-top: 3px; letter-spacing: 0.2px; }
</style>
</head>
<body>
  <main class="menu-poster">
    <div class="product-photo product-photo--small" role="img" aria-label="Small cup of vanilla frozen yogurt topped with kiwi, blueberries and blackberries"></div>
    <div class="price-badge price-badge--small">
      <span class="price-badge__size">Small</span>
      <span class="price-badge__amount">$4</span>
    </div>

    <div class="price-badge price-badge--medium">
      <span class="price-badge__size">Medium</span>
      <span class="price-badge__amount">$6</span>
    </div>
    <div class="product-photo product-photo--medium" role="img" aria-label="Medium cup of chocolate frozen yogurt topped with strawberries and raspberries"></div>

    <div class="product-photo product-photo--large" role="img" aria-label="Large cup of vanilla frozen yogurt topped with strawberries, blueberries and blackberries"></div>
    <div class="price-badge price-badge--large">
      <span class="price-badge__size">Large</span>
      <span class="price-badge__amount">$8</span>
    </div>

    <div class="topping-note">
      <div class="topping-note__price">Extra $0.50</div>
      <div class="topping-note__label">For each toppings</div>
      <div class="topping-note__list">(Stawberries, kiwi, nuts, candy, etc)</div>
    </div>
  </main>
</body>
</html>
```